Inspire Design with Natural Stone: Quarrell Ltd. Tradeshow Booth Backdrop

Client: Quarrell Ltd.
Project Goal: To design a visually compelling and informative 7.5ft x 10ft backdrop for Quarrell Ltd.'s 10ft x 10ft tradeshow booth that attracts and engages architects, designers, homeowners, and contractors, ultimately driving interest in their natural stone products.
Quarrell Ltd. is a leading provider of high-quality natural stone for a wide range of residential and commercial projects. We offer a diverse selection of stone types, finishes, and applications, known for their beauty, durability, and timeless appeal. We are participating in upcoming tradeshows to generate new leads, strengthen brand awareness, and showcase our latest offerings to key target audiences.
Target Audience(s):
Architects: Seeking premium, unique, and sustainable natural stone options for their designs, with an appreciation for quality and aesthetic integration.
Designers (Interior & Landscape): Looking for visually appealing and versatile stone to enhance their projects, focusing on texture, color palettes, and application possibilities.
Homeowners: Aspiring to elevate their living spaces with natural stone, driven by aesthetics, durability, and adding lasting value to their homes.
Contractors: Seeking reliable and high-quality stone suppliers for their building and renovation projects, prioritizing ease of installation and client satisfaction.
Key Message/Desired Outcome: We want our booth to communicate that Quarrell Ltd. is the premier source for beautiful, high-quality natural stone solutions for any project, backed by expertise and a commitment to customer satisfaction. We want to inspire visitors with the possibilities of using natural stone in their designs and projects.
Mandatories:
* Backdrop Dimensions: 7.5 feet (height) x 10 feet (width). (See attached template)
* Inclusion of Quarrell Ltd. Logo:* The logo must be prominently featured and easily recognizable. Please refer to the attached brand guidelines for logo usage, color palette, and typography.
*Clear Representation of Natural Stone: The design must showcase the beauty and variety of Quarrell Ltd.'s natural stone products. This can be achieved through high-quality photography, subtle textures, or artistic representations. Please use our website's photo and project gallery.
*Contact Information: Include our website address: www.quarrellbrix.example
Optional Elements (Consideration):
*Visuals of Applications: Showcasing natural stone used in various settings (e.g., fireplaces, facades, patios, interior walls) could be impactful.
*Highlighting Key Benefits: Briefly communicating the advantages of natural stone (e.g., durability, sustainability, timelessness).
*Integration of Textures: Subtly incorporating textures that hint at the feel of natural stone.
Look and Feel:
*Overall Impression: Sophisticated, natural, high-quality, inviting, trustworthy, and inspiring.
*Style: Clean, modern, and visually appealing, allowing the beauty of the stone to take center stage. Avoid overly busy or cluttered designs.
*Color Palette: Primarily utilize Quarrell Ltd.'s brand colors (refer to brand guidelines).
Things to Avoid:
* Generic stock imagery that doesn't accurately represent Quarrell's products.
* Cluttered layouts with excessive text.
* Designs that appear cheap or unprofessional.
* Difficult-to-read fonts or color combinations.
Deliverables:
* High-resolution digital design file(s) suitable for large-format printing (AI, Photoshop, PDF).
* Mockup of the backdrop design within a 10ft x 10ft booth space. Please feel free to include any other booth features (tables, flooring, etc) that you think would work well with the backdrop (optional but highly recommended).
We are excited to see your creative interpretations and look forward to selecting a design that will make a strong and lasting impression at our upcoming tradeshows!

```html
<!DOCTYPE html>
<html lang="en">
<head>
<meta charset="utf-8">
<title>Quarrell Ltd. Tradeshow Backdrop</title>
<link rel="stylesheet" href="https://fonts.googleapis.com/css2?family=Exo+2:ital,wght@0,400;0,500;0,600;1,600&display=swap">
<style>
  :root {
    --stage: #9b9b9b;
    --paper: #ffffff;
    --ink: #1a1f2b;
    --haze: #f1f1f1;
    --rule: #e4e4e4;
    --sand: #c9c8ae;
    --moss: #6f8a4a;
    --stone-light: #cfc3b0;
    --stone: #a8957c;
    --timber: #7a4a2a;
  }
  html, body {
    margin: 0;
    width: 1200px;
    height: 1200px;
    overflow: hidden;
    background: var(--stage);
  }
  .backdrop {
    position: absolute;
    left: 40px;
    top: 180px;
    width: 1120px;
    height: 840px;
    background: var(--paper);
  }
  .backdrop svg { display: block; width: 100%; height: 100%; }
  .headline {
    font-family: "Exo 2", sans-serif;
    font-style: italic;
    font-weight: 600;
    font-size: 30px;
    letter-spacing: 0.6px;
    fill: var(--ink);
  }
  .benefit {
    font-family: "Exo 2", sans-serif;
    font-weight: 400;
    font-size: 19px;
    fill: var(--ink);
  }
  .brand-name {
    font-family: "Exo 2", sans-serif;
    font-weight: 600;
    font-size: 26px;
    letter-spacing: 0.5px;
    fill: var(--ink);
  }
  .web-address {
    font-family: "Exo 2", sans-serif;
    font-weight: 500;
    font-size: 19px;
    letter-spacing: 3px;
    fill: var(--ink);
  }
  .haze-shape { fill: var(--haze); }
  .accent-rule { fill: var(--rule); }
  .cut-stripe { fill: var(--paper); }
  .benefit-band { fill: var(--sand); }
  .brand-square { fill: var(--ink); }
</style>
</head>
<body>
<main class="backdrop">
  <svg viewBox="0 0 784 587" xmlns="http://www.w3.org/2000/svg">
    <defs>
      <linearGradient id="stone-wall-tones" x1="0" y1="1" x2="1" y2="0">
        <stop offset="0" stop-color="var(--moss)"/>
        <stop offset="0.22" stop-color="#8f9a6a"/>
        <stop offset="0.4" stop-color="var(--stone-light)"/>
        <stop offset="0.7" stop-color="var(--stone)"/>
        <stop offset="0.92" stop-color="var(--timber)"/>
      </linearGradient>
    </defs>

    <polygon class="haze-shape" points="0,80 80,0 120,0 360,240 120,440 0,440"/>
    <polygon class="accent-rule" points="10,450 170,290 182,290 22,450"/>
    <polygon class="accent-rule" points="0,505 190,320 202,320 12,505"/>

    <polygon class="stone-photo" role="img"
      aria-label="Photograph of a rounded fieldstone wall with timber beams above and green plantings at its base"
      fill="url(#stone-wall-tones)"
      points="0,500 180,355 330,355 425,265 500,265 690,0 784,0 784,84 452,404 372,504 340,587 0,587"/>

    <polygon class="cut-stripe" points="150,587 330,370 350,370 172,587"/>
    <polygon class="cut-stripe" points="0,560 70,495 80,495 0,572"/>

    <polygon class="benefit-band" points="452,404 784,404 784,499 372,499 372,490"/>

    <text class="headline">
      <tspan x="57" y="93">BRIEFLY</tspan>
      <tspan x="57" y="137">COMMUNICATING</tspan>
      <tspan x="57" y="182">THE ADVANTAGES</tspan>
      <tspan x="57" y="227">OF NATURAL STONE</tspan>
    </text>

    <rect class="brand-square" x="560" y="339" width="16" height="16"/>
    <text class="brand-name" x="584" y="357">QUARRELL</text>

    <text class="benefit" text-anchor="end">
      <tspan x="718" y="427">Subtly incorporating</tspan>
      <tspan x="718" y="454">textures that hint at the</tspan>
      <tspan x="718" y="482">feel of natural stone.</tspan>
    </text>

    <text class="web-address" x="720" y="544" text-anchor="end">www.quarrellbrix.example</text>
  </svg>
</main>
</body>
</html>
```